The Quillmore Daily Ledger

I am making a journal for tracking pain symptoms for TMJ (Jaw) pain. I have the cover designed and I just need the journal page designed that will repeat throughout the journal. The journal is the image on the left of the bundle. The page I would like to be developed is the picture that I hand sketched out. It should be a 6 x 9 page, similar to the attached example. Greyscale, no color. Thank you!

Target Market(s)

20-55 year old women

Industry/Entity Type

Healthcare

Colors

Designer to choose only greyscale colors for use in the design.

Requirements
Must have
• A neat, well-designed page with the content I have sketched out by hand.
Nice to have
• Creative display of the content I provided and development of the pain scale and pain diagram faces in a professional looking way.

```html
<!DOCTYPE html>
<html lang="en">
<head>
<meta charset="utf-8">
<title>The Quillmore Daily Ledger – Daily Page</title>
<link href="https://fonts.googleapis.com/css2?family=Questrial&display=swap" rel="stylesheet">
<style>
  :root{
    --ink:#4a4a4a;
    --band:#575757;
    --cell:#d9d9d9;
    --cell-soft:#e6e6e6;
    --panel:#e3e3e3;
    --paper:#ffffff;
    --backdrop:#cfcfcf;
    --rule:#6a6a6a;
  }
  *{box-sizing:border-box;margin:0;padding:0}
  html,body{width:1068px;height:1200px;overflow:hidden}
  body{background:var(--backdrop);font-family:"Questrial",sans-serif;color:var(--ink)}
  .page{position:absolute;left:154px;top:30px;width:760px;height:1140px;background:var(--paper);
        border-top:14px solid var(--band);border-bottom:14px solid var(--band);padding:18px 40px 0}
  .header{display:flex;justify-content:space-between;align-items:center;height:70px}
  .brand{display:flex;align-items:center;gap:12px;font-size:20px;color:var(--band)}
  .brand-dot{width:44px;height:44px;border-radius:50%;border:3px solid var(--band)}
  .date{display:flex;align-items:center;width:330px;height:34px;border:1.5px solid #999;border-radius:17px;overflow:hidden}
  .date-tag{background:var(--band);color:#fff;height:100%;padding:0 26px;display:flex;align-items:center;border-radius:17px;font-size:17px;letter-spacing:1px}
  .bar{height:30px;border-radius:15px;background:var(--band);color:#fff;text-align:center;font-size:17px;line-height:30px;letter-spacing:.5px;text-transform:uppercase;margin:12px 0 10px}
  .bar small{text-transform:none;font-size:17px}
  .time{display:flex;gap:24px}
  .time-table{flex:1;display:grid;grid-template-columns:22px 1fr 1fr 1fr;gap:4px}
  .time-table .hd{background:var(--cell-soft);font-size:13px;text-align:center;padding:3px 0}
  .time-table .num{background:var(--cell-soft);font-size:13px;text-align:center;line-height:22px}
  .time-table .slot{background:var(--cell);height:22px}
  .scale{display:grid;grid-template-columns:repeat(5,1fr);gap:6px}
  .grade{text-align:center}
  .grade-top{display:flex;justify-content:center;align-items:center;gap:10px;font-size:14px;height:40px}
  .face-icon{width:30px;height:30px;border-radius:50%;border:1.5px solid var(--ink)}
  .grade-label{background:var(--cell);font-size:14px;padding:4px 0}
  .body-row{display:flex;gap:10px;margin-top:14px}
  .diagrams{flex:1;display:grid;grid-template-columns:repeat(5,1fr);gap:8px;background:var(--cell-soft);padding:10px}
  .spot{display:flex;flex-direction:column;align-items:center;gap:6px}
  .spot-art{width:88px;height:92px;background:linear-gradient(#f6f6f6,#d3d3d3);border-radius:8px}
  .spot-label{background:var(--cell);font-size:14px;width:88px;text-align:center;padding:2px 0}
  .rating{display:flex}
  .rating span{width:15px;height:15px;border:1.5px solid var(--ink);margin-left:-1.5px;background:#fff}
  .status{width:200px;background:var(--panel);padding:14px 12px;display:flex;flex-direction:column;gap:16px}
  .status-group{display:flex;gap:10px;align-items:center}
  .status-name{width:70px;font-size:14px;line-height:1.2;text-align:center}
  .opt{display:flex;align-items:center;gap:6px;font-size:13px;line-height:1.35}
  .box{display:inline-block;width:13px;height:13px;border:1.5px solid var(--ink);flex:none;background:#fff}
  .checks{display:grid;grid-template-columns:1fr 1fr 1fr;gap:4px 20px;font-size:14px}
  .checks .opt{font-size:14px;line-height:1.5}
  .line-fill{flex:1;border-bottom:1px solid var(--rule);height:14px}
  .state{margin-top:10px;display:flex;flex-direction:column;gap:6px;font-size:14px}
  .state-row{display:flex;align-items:center;gap:14px}
  .state-row .lead{width:150px}
  .state-row .opt{font-size:14px;margin-right:8px}
  .notes{margin-top:8px}
  .notes div{border-bottom:1px solid var(--rule);height:30px}
</style>
</head>
<body>
<main class="page">
  <header class="header">
    <div class="brand"><span class="brand-dot"></span>The Quillmore Daily Ledger</div>
    <div class="date"><span class="date-tag">DATE</span></div>
  </header>

  <div class="bar">Time</div>
  <section class="time">
    <div class="time-table">
      <span></span><span class="hd">begin</span><span class="hd">end</span><span class="hd">duration</span>
      <span class="num">1</span><span class="slot"></span><span class="slot"></span><span class="slot"></span>
      <span class="num">2</span><span class="slot"></span><span class="slot"></span><span class="slot"></span>
      <span class="num">3</span><span class="slot"></span><span class="slot"></span><span class="slot"></span>
    </div>
    <div class="time-table">
      <span></span><span class="hd">begin</span><span class="hd">end</span><span class="hd">duration</span>
      <span class="num">4</span><span class="slot"></span><span class="slot"></span><span class="slot"></span>
      <span class="num">5</span><span class="slot"></span><span class="slot"></span><span class="slot"></span>
      <span class="num">6</span><span class="slot"></span><span class="slot"></span><span class="slot"></span>
    </div>
  </section>

  <div class="bar">Severity of Pain</div>
  <section class="scale">
    <div class="grade"><div class="grade-top">1<span class="face-icon" role="img" aria-label="mild pain face icon"></span>2</div><div class="grade-label">Mild</div></div>
    <div class="grade"><div class="grade-top">3<span class="face-icon" role="img" aria-label="moderate pain face icon"></span>4</div><div class="grade-label">Moderate</div></div>
    <div class="grade"><div class="grade-top">5<span class="face-icon" role="img" aria-label="severe pain face icon"></span>6</div><div class="grade-label">Severe</div></div>
    <div class="grade"><div class="grade-top">7<span class="face-icon" role="img" aria-label="very severe pain face icon"></span>8</div><div class="grade-label">Very Severe</div></div>
    <div class="grade"><div class="grade-top">9<span class="face-icon" role="img" aria-label="worst pain face icon"></span>10</div><div class="grade-label">Worst</div></div>
  </section>

  <section class="body-row">
    <div class="diagrams">
      <div class="spot"><div class="spot-art" role="img" aria-label="head profile marking the jaw joint"></div><div class="spot-label">Joint</div><div class="rating"><span></span><span></span><span></span><span></span><span></span></div></div>
      <div class="spot"><div class="spot-art" role="img" aria-label="head profile marking jaw muscles"></div><div class="spot-label">Muscles</div><div class="rating"><span></span><span></span><span></span><span></span><span></span></div></div>
      <div class="spot"><div class="spot-art" role="img" aria-label="head profile marking the neck"></div><div class="spot-label">Neck</div><div class="rating"><span></span><span></span><span></span><span></span><span></span></div></div>
      <div class="spot"><div class="spot-art" role="img" aria-label="front head view marking forehead tension"></div><div class="spot-label">Tension</div><div class="rating"><span></span><span></span><span></span><span></span><span></span></div></div>
      <div class="spot"><div class="spot-art" role="img" aria-label="drawing of teeth"></div><div class="spot-label">Teeth</div><div class="rating"><span></span><span></span><span></span><span></span><span></span></div></div>
    </div>
    <div class="status">
      <div class="status-group">
        <div class="status-name">Click/<br>Pop</div>
        <div><div class="opt"><span class="box"></span>Increase</div><div class="opt"><span class="box"></span>Decrease</div><div class="opt"><span class="box"></span>No Change</div></div>
      </div>
      <div class="status-group">
        <div class="status-name">Opening<br>Ability</div>
        <div><div class="opt"><span class="box"></span>Increase</div><div class="opt"><span class="box"></span>Decrease</div><div class="opt"><span class="box"></span>No Change</div></div>
      </div>
    </div>
  </section>

  <div class="bar">Triggers <small>(Check all that apply)</small></div>
  <section class="checks">
    <div><div class="opt"><span class="box"></span>Sleep</div><div class="opt"><span class="box"></span>First thing in AM</div><div class="opt"><span class="box"></span>Clencing</div><div class="opt"><span class="box"></span>Insomnia</div></div>
    <div><div class="opt"><span class="box"></span>Weather</div><div class="opt"><span class="box"></span>Eating</div><div class="opt"><span class="box"></span>Work</div><div class="opt"><span class="box"></span>Opening wide/Yawn</div></div>
    <div><div class="opt"><span class="box"></span>PMS/Mensturation</div><div class="opt"><span class="box"></span>Stress at Home</div><div class="opt"><span class="box"></span>Stress at Work</div><div class="opt"><span class="box"></span>Other<span class="line-fill"></span></div></div>
  </section>
  <section class="state">
    <div class="state-row"><span class="lead">My Jaw was</span><span class="opt"><span class="box"></span>Relaxed</span><span class="opt"><span class="box"></span>Clenched</span><span class="opt"><span class="box"></span>Tense</span></div>
    <div class="state-row"><span class="lead">My breathing was</span><span class="opt"><span class="box"></span>Deep/Relaxed</span><span class="opt"><span class="box"></span>Shallow/Tense</span></div>
    <div class="state-row"><span class="lead">My Neck/Shoulder were</span><span class="opt"><span class="box"></span>Relaxed</span><span class="opt"><span class="box"></span>Tense</span><span class="opt"><span class="box"></span>Slouched</span><span class="opt"><span class="box"></span>Upright</span></div>
  </section>

  <div class="bar">Relief Measures <small>(Check all that apply)</small></div>
  <section class="checks">
    <div><div class="opt"><span class="box"></span>Deep breathing</div><div class="opt"><span class="box"></span>Teeth apart/relax/jaw</div><div class="opt"><span class="box"></span>Self-massage</div><div class="opt"><span class="box"></span>Heat/cold (circle)</div></div>
    <div><div class="opt"><span class="box"></span>Medication</div><div class="opt"><span class="box"></span>Rest</div><div class="opt"><span class="box"></span>Gentle Stretching</div><div class="opt"><span class="box"></span>Posture correction</div></div>
    <div><div class="opt"><span class="box"></span>Mind reset</div><div class="opt"><span class="box"></span>Stabilization Exercise</div><div class="opt"><span class="box"></span>Other<span class="line-fill"></span></div><div class="opt"><span class="box"></span><span class="line-fill"></span></div></div>
  </section>

  <div class="bar">Notes and Plan to Avoid Triggers</div>
  <section class="notes"><div></div><div></div><div></div><div></div><div></div></section>
</main>
</body>
</html>
```